Korvex TR40 Graphics Car Wrap/ Universal Car/small truck Wrap

Logo on door, stick to colour design, optionally add key points(services). I am relying on the expertise of the graphics designers to come up with something I can use on all my vehicles.

Somewhere discrete the pelnor number and lic number needs to be displayed like in the toolbox image.

The vehicle is a Korvex TR-40 2024 varluma model

```html
<!DOCTYPE html>
<html lang="en">
<head>
<meta charset="utf-8">
<title>Tervalo Energy – Vehicle Door Graphics</title>
<link href="https://fonts.googleapis.com/css2?family=Montserrat:wght@500;600;700&display=swap" rel="stylesheet">
<style>
  :root {
    --navy: #1a2a9a;
    --royal: #0a2fd6;
    --green: #6cb33f;
    --white: #ffffff;
    --panel-edge: #e3e6ea;
    --page: #ffffff;
  }
  html, body {
    margin: 0;
    padding: 0;
    width: 1200px;
    height: 1022px;
    overflow: hidden;
    background: var(--page);
    font-family: "Montserrat", sans-serif;
  }
  .wrap-sheet {
    position: relative;
    width: 1200px;
    height: 1022px;
  }
  .door-panel {
    position: absolute;
    left: 120px;
    width: 960px;
    height: 380px;
  }
  .door-panel--driver { top: 90px; }
  .door-panel--passenger { top: 552px; }
  .panel-base { fill: var(--white); stroke: var(--panel-edge); stroke-width: 2; }
  .service-block { fill: var(--royal); }
  .info-band { fill: var(--green); }
  .brand-name { fill: var(--navy); font-weight: 600; font-size: 54px; letter-spacing: -0.5px; }
  .service-item { fill: var(--white); font-weight: 600; font-size: 28px; letter-spacing: 0.5px; }
  .web-address { fill: var(--white); font-weight: 500; font-size: 21px; letter-spacing: 0.5px; }
  .phone-number { fill: var(--white); font-weight: 700; font-size: 23px; }
  .licence-note { fill: var(--white); font-weight: 500; font-size: 12px; }
</style>
</head>
<body>
<main class="wrap-sheet">

  <svg class="door-panel door-panel--driver" viewBox="0 0 960 380" role="group" aria-label="Driver side door graphics">
    <rect class="panel-base" x="1" y="1" width="958" height="378"/>
    <path class="service-block" d="M860 0 H960 V380 H560 L780 40 Q805 0 860 0 Z"/>
    <rect class="info-band" x="0" y="265" width="960" height="46"/>
    <text class="brand-name" x="50" y="215">TERVALO ENERGY</text>
    <g text-anchor="end">
      <text class="service-item" x="935" y="72">SOLAR</text>
      <text class="service-item" x="935" y="122">AIR CON</text>
      <text class="service-item" x="935" y="172">BATTERIES</text>
      <text class="service-item" x="935" y="222">ELECTRICAL</text>
    </g>
    <text class="web-address" x="50" y="296">TERVALOENERGY.COM.AU</text>
    <text class="phone-number" x="380" y="296">48 512 307</text>
    <text class="licence-note" x="660" y="293">LIC: 40917</text>
    <text class="licence-note" x="760" y="293">PELNOR: AU31804</text>
  </svg>

  <svg class="door-panel door-panel--passenger" viewBox="0 0 960 380" role="group" aria-label="Passenger side door graphics">
    <rect class="panel-base" x="1" y="1" width="958" height="378"/>
    <path class="service-block" d="M100 0 H0 V380 H400 L180 40 Q155 0 100 0 Z"/>
    <rect class="info-band" x="0" y="265" width="960" height="46"/>
    <text class="brand-name" x="910" y="215" text-anchor="end">TERVALO ENERGY</text>
    <text class="service-item" x="25" y="72">SOLAR</text>
    <text class="service-item" x="25" y="122">AIR CON</text>
    <text class="service-item" x="25" y="172">BATTERIES</text>
    <text class="service-item" x="25" y="222">ELECTRICAL</text>
    <text class="licence-note" x="40" y="293">LIC: 40917</text>
    <text class="licence-note" x="140" y="293">PELNOR: AU31804</text>
    <text class="phone-number" x="420" y="296">48 512 307</text>
    <text class="web-address" x="910" y="296" text-anchor="end">TERVALOENERGY.COM.AU</text>
  </svg>

</main>
</body>
</html>
```